Brell Harbor Company Business Cards

Front and Back Business Card - logo and text setup - cool design. I need workable photoshop or illustrator files so I can setup each employee card with design that is created
Updates

Hi everyone, thank you for the great entries. Please no more white and blue cards - there are so many already - black and silver only now please. thanks!

Target Market(s)

Construction Industry - Facility Managers

Industry/Entity Type

Construction

Contact Information for Business Card

I really like contemporary simplistic looks - clean neat....not opposed to seeing some black backrounds

Requirements
Must have
• Logo/website address with design on front only - www.brellharbor-example.com (logo attached)
• Back:
• Name/Title/Company Address/Phone/email address
Nice to have
• Cool design
Should not have
• Nothing gimmicky like Fire or Water - since we are a Fire Protection company - it has all been done

```html
<!DOCTYPE html>
<html lang="en">
<head>
<meta charset="utf-8">
<title>Brell Harbor Company – Business Cards</title>
<link href="https://fonts.googleapis.com/css2?family=Open+Sans:wght@400;600;800&display=swap" rel="stylesheet">
<style>
  :root {
    --backdrop: #2b2b2d;
    --card: #131315;
    --card-edge: #26262a;
    --silver: #c4c8cd;
    --silver-deep: #8d9299;
    --ink: #f0f0f0;
    --muted: #cfd2d6;
  }
  * { box-sizing: border-box; margin: 0; padding: 0; }
  html, body {
    width: 1200px; height: 716px; overflow: hidden;
    background: var(--backdrop);
    font-family: "Open Sans", Arial, sans-serif;
  }
  .stage { position: relative; width: 1200px; height: 716px; }
  .card {
    position: absolute;
    width: 520px; height: 300px;
    background: var(--card);
    border: 1px solid var(--card-edge);
    border-radius: 18px;
    box-shadow: 0 14px 30px rgba(0,0,0,.45);
  }
  .card--front { left: 50px; top: 90px; }
  .card--back { left: 630px; top: 326px; }

  .front-mark {
    position: absolute; left: 0; right: 0; top: 104px;
    display: flex; align-items: center; justify-content: center; gap: 14px;
  }
  .front-mark__dot {
    width: 18px; height: 18px; background: var(--silver); border-radius: 50%;
  }
  .front-mark__name {
    font-weight: 800; font-size: 46px; line-height: 60px;
    color: var(--silver); letter-spacing: -.5px;
  }
  .front-web {
    position: absolute; left: 0; right: 0; top: 178px;
    text-align: center; color: var(--silver-deep);
    font-size: 14px; letter-spacing: 1px;
  }

  .holder { position: absolute; left: 36px; top: 34px; }
  .holder__name { color: var(--ink); font-size: 20px; font-weight: 400; letter-spacing: .5px; }
  .holder__title { color: var(--silver-deep); font-size: 12px; margin-top: 2px; letter-spacing: .5px; }
  .holder__rule { width: 60px; height: 2px; background: var(--silver); margin-top: 8px; }

  .contact { position: absolute; left: 36px; top: 150px; list-style: none; }
  .contact li {
    color: var(--muted); font-size: 13px; line-height: 22px;
    display: flex; align-items: center; gap: 10px;
  }
  .contact svg { width: 12px; height: 12px; flex: none; }

  .back-mark {
    position: absolute; right: 30px; top: 36px;
    display: flex; align-items: center; gap: 10px;
  }
  .back-mark__dot { width: 12px; height: 12px; background: var(--silver); border-radius: 50%; }
  .back-mark__name { font-weight: 800; font-size: 26px; color: var(--silver); }
</style>
</head>
<body>
<main class="stage">
  <section class="card card--front" aria-label="Card front">
    <div class="front-mark">
      <span class="front-mark__dot"></span>
      <span class="front-mark__name">Brell Harbor</span>
    </div>
    <p class="front-web">www.brellharbor-example.com</p>
  </section>

  <section class="card card--back" aria-label="Card back">
    <div class="holder">
      <p class="holder__name">YOUR NAME</p>
      <p class="holder__title">JOB TITLE</p>
      <div class="holder__rule"></div>
    </div>
    <ul class="contact">
      <li>
        <svg viewBox="0 0 12 12"><path d="M2 1h2.5l1 3-1.5 1a6 6 0 0 0 3 3l1-1.5 3 1V10a1 1 0 0 1-1 1A9 9 0 0 1 1 2a1 1 0 0 1 1-1z" fill="var(--silver)"/></svg>
        000 000 0000
      </li>
      <li>
        <svg viewBox="0 0 12 12"><rect x="1" y="2.5" width="10" height="7" fill="var(--silver)"/><path d="M1 2.5l5 4 5-4" stroke="var(--card)" fill="none"/></svg>
        youremail@xyz.com
      </li>
      <li>
        <svg viewBox="0 0 12 12"><circle cx="6" cy="6" r="4.8" fill="none" stroke="var(--silver)" stroke-width="1.2"/><path d="M1.2 6h9.6M6 1.2c-2.4 2.6-2.4 7 0 9.6M6 1.2c2.4 2.6 2.4 7 0 9.6" stroke="var(--silver)" fill="none" stroke-width=".9"/></svg>
        www.brellharbor-example.com
      </li>
      <li>00, Somewhere, Anywhere</li>
      <li>City, ST 0000</li>
    </ul>
    <div class="back-mark">
      <span class="back-mark__dot"></span>
      <span class="back-mark__name">Brell Harbor</span>
    </div>
  </section>
</main>
</body>
</html>
```